Birchford Realty Business Card

Business Card:

Somewhere on front of card, please include Broker License Number: 5839162

Website is BirchfordRealty.example

Address is:
7218 Crestover Ave E
Saginaw, MI 48271

I'll let you use creative freedom on the rest; we obviously need Name, Title, Email (@BirchfordRealty.example), Office Phone, Cell Phone.

Don't want any special die-cutting, just a standard size business card.

On the back, include a place for the date and time of an appointment to be written in pen.

Requirements
Must have
• Our logo, attached to email.

```html
<!DOCTYPE html>
<html lang="en">
<head>
<meta charset="utf-8">
<title>Birchford Realty Business Card</title>
<link href="https://fonts.googleapis.com/css2?family=Ubuntu:wght@400;500;700&display=swap" rel="stylesheet">
<style>
  :root {
    --navy: #2e1f6e;
    --navy-soft: rgba(46, 31, 110, 0.14);
    --stone: #a9a8a9;
    --stone-dark: #9c9b9c;
    --paper: #ffffff;
    --backdrop: #ecebec;
    --white: #ffffff;
  }
  * { margin: 0; padding: 0; box-sizing: border-box; }
  html, body { width: 1200px; height: 1200px; overflow: hidden; }
  body {
    background: var(--backdrop);
    font-family: "Ubuntu", sans-serif;
    position: relative;
  }
  .card { position: absolute; overflow: hidden; }

  /* Appointment side */
  .card--appointment {
    left: 238px; top: 119px; width: 714px; height: 419px;
    background: var(--paper);
  }
  .appointment-tab {
    position: absolute; left: 0; top: 101px; width: 362px; height: 47px;
    background: var(--stone);
    clip-path: polygon(0 0, 345px 0, 362px 100%, 0 100%);
  }
  .appointment-tab__label {
    position: absolute; left: 48px; top: 11px;
    font-weight: 700; font-size: 23px; letter-spacing: 1px;
    color: var(--navy); word-spacing: 4px;
  }
  .brand-name {
    font-family: "Ubuntu", sans-serif;
    font-weight: 500; color: var(--navy); white-space: nowrap;
  }
  .card--appointment .brand-name {
    position: absolute; right: 54px; top: 96px; font-size: 35px;
  }
  .field {
    position: absolute; display: flex; align-items: flex-end;
    font-size: 18px; color: var(--navy);
  }
  .field__rule {
    border-bottom: 1.5px solid var(--navy); height: 20px; margin-left: 5px;
  }
  .field--for { left: 48px; top: 212px; }
  .field--for .field__rule { width: 584px; }
  .field--date { left: 48px; top: 282px; }
  .field--date .field__rule { width: 296px; }
  .field--time { left: 401px; top: 282px; }
  .field--time .field__rule { width: 210px; }
  .license-band {
    position: absolute; left: 0; bottom: 0; width: 100%; height: 57px;
    background: var(--navy); color: var(--white);
    font-size: 18px; display: flex; align-items: center; justify-content: center;
    letter-spacing: 0.3px;
  }

  /* Contact side */
  .card--contact {
    left: 230px; top: 644px; width: 713px; height: 418px;
    background: linear-gradient(90deg, var(--stone-dark), var(--stone) 40%, var(--stone));
  }
  .card__accent-area {
    position: absolute; left: 0; top: 0; width: 240px; height: 100%;
    background: linear-gradient(135deg, var(--navy-soft), rgba(255, 255, 255, 0) 70%);
  }
  .card--contact .brand-name {
    position: absolute; left: 34px; top: 204px; font-size: 36px;
  }
  .person { position: absolute; left: 365px; top: 75px; }
  .person__name { font-weight: 700; font-size: 25px; color: var(--navy); letter-spacing: 0.5px; }
  .person__title { font-size: 16px; color: var(--white); margin-top: 8px; }
  .contact-list { position: absolute; left: 366px; top: 176px; list-style: none; }
  .contact-list__item {
    display: flex; align-items: center; height: 23.5px;
    font-size: 18px; color: var(--white); letter-spacing: 0.2px;
  }
  .contact-list__icon { width: 18px; height: 18px; margin-right: 18px; flex: none; }
  .address {
    position: absolute; left: 366px; top: 289px;
    font-size: 18px; line-height: 25px; color: var(--white); font-style: normal;
  }
</style>
</head>
<body>

<section class="card card--appointment">
  <div class="appointment-tab"><span class="appointment-tab__label">YOUR APPOINTMENT</span></div>
  <div class="brand-name">Birchford Realty</div>
  <div class="field field--for">For<span class="field__rule"></span></div>
  <div class="field field--date">Date:<span class="field__rule"></span></div>
  <div class="field field--time">Time:<span class="field__rule"></span></div>
  <div class="license-band">Broker License Number: 5839162</div>
</section>

<section class="card card--contact">
  <div class="card__accent-area" role="img" aria-label="Decorative angled line pattern in navy and white"></div>

  <div class="brand-name">Birchford Realty</div>

  <div class="person">
    <div class="person__name">Your XYZ Name</div>
    <div class="person__title">Your Title</div>
  </div>

  <ul class="contact-list">
    <li class="contact-list__item">
      <svg class="contact-list__icon" viewBox="0 0 18 18" aria-hidden="true"><rect x="4" y="1" width="10" height="16" rx="1.5" fill="#2e1f6e"/><rect x="6" y="3.5" width="6" height="9" fill="#ffffff"/></svg>
      +00 111 222 3333
    </li>
    <li class="contact-list__item">
      <svg class="contact-list__icon" viewBox="0 0 18 18" aria-hidden="true"><path d="M2 6 Q9 1 16 6 L14 8 L12 6.5 L6 6.5 L4 8 Z" fill="#2e1f6e"/><rect x="4" y="9" width="10" height="7" rx="1" fill="#2e1f6e"/></svg>
      +00 111 444 5555
    </li>
    <li class="contact-list__item">
      <svg class="contact-list__icon" viewBox="0 0 18 18" aria-hidden="true"><circle cx="9" cy="9" r="6.5" fill="#2e1f6e"/><path d="M2.5 9 H15.5 M9 2.5 V15.5 M4 5.5 H14 M4 12.5 H14" stroke="#a9a8a9" stroke-width="0.9"/></svg>
      www.BirchfordRealty.example
    </li>
    <li class="contact-list__item">
      <svg class="contact-list__icon" viewBox="0 0 18 18" aria-hidden="true"><rect x="2" y="4" width="14" height="10" fill="#2e1f6e"/><path d="M2 4 L9 10 L16 4 M2 14 L7 9 M16 14 L11 9" stroke="#a9a8a9" stroke-width="1" fill="none"/></svg>
      yourname@BirchfordRealty.example
    </li>
  </ul>

  <address class="address">7218 Crestover Ave E<br>Saginaw, MI 48271</address>
</section>

</body>
</html>
```